LINGERIE WEBSHOP - Velora casa

We are looking for design and layout design for our webshop. We are company that sells lingerie and other connected textile products liki payamas and etc..
Our website will have approx 500 different products within 2 main catogories Woman/Man) and approx. 10 subcategories
Here is what we expect form design:
-Color pallete should be black and white (if you wish you can add some accent color)
-we want to leave feeling to customers of good quality products towards to luxury
-UX should be simple. Feel free to suggest layout
-frontpage layout, product list layout, product description layout, blog layout
-responsive design, compatible with smartphone

Target Market(s)

woman buying for themself, man buying for woman

Industry/Entity Type

Lingerie

Logo Text

VELORA CASA

Number of Pages Required

4 page

Font styles to use
Sans Serif
Decorative

Requirements
Must have
• simple UX
Nice to have
• difference for sexy/luxury lingerie and daily/cozy lingerie
Should not have
• cheap feel, unreliable

```html
<!DOCTYPE html>
<html lang="en">
<head>
<meta charset="utf-8">
<title>Velora casa – Lingerie webshop</title>
<link href="https://fonts.googleapis.com/css2?family=Lato:wght@400;700&family=Lobster+Two:ital,wght@1,700&family=Dancing+Script:wght@400;500&display=swap" rel="stylesheet">
<style>
:root{
  --ink:#1b1b1b;
  --text:#4a4a4a;
  --muted:#7a7a7a;
  --line:#e7e7e7;
  --paper:#ffffff;
  --band:#f6f6f6;
  --pattern:#f1f1f1;
  --footer:#f4f4f4;
  --bottom:#8c8c8c;
  --sans:'Lato',Arial,sans-serif;
  --head:'Lobster Two',Georgia,cursive;
  --script:'Dancing Script',Georgia,cursive;
}
*{box-sizing:border-box;margin:0;padding:0}
html,body{width:1200px;height:2990px;overflow:hidden}
body{position:relative;background:var(--paper);font-family:var(--sans);color:var(--text)}
.abs{position:absolute}
a{color:inherit;text-decoration:none}

/* header */
.site-header{top:0;left:0;width:1200px;height:67px;background:var(--paper);border-bottom:1px solid var(--line)}
.brand{left:128px;top:22px;font-family:var(--sans);font-size:25px;letter-spacing:1px;color:var(--ink)}
.main-nav{left:369px;top:27px;display:flex;gap:28px;font-size:11.5px;text-transform:uppercase;color:var(--text)}
.main-nav .has-sub::after{content:"";display:inline-block;width:4px;height:4px;border-right:1px solid var(--muted);border-bottom:1px solid var(--muted);transform:rotate(45deg);margin-left:8px;position:relative;top:-3px}
.header-tools{left:956px;top:24px;display:flex;gap:24px;align-items:center;font-size:12px}
.header-tools svg{width:17px;height:17px;stroke:var(--text);fill:none;stroke-width:1.4}

/* hero */
.hero{top:67px;left:0;width:1200px;height:481px;background:linear-gradient(90deg,#c8a38a 0%,#3b302d 14%,#6c5a52 27%,#a7ab9f 40%,#c6cdbe 62%,#9fb08c 85%,#b9c4ad 100%)}
.hero-panel{top:125px;left:569px;width:502px;height:365px;background:rgba(248,248,248,.88);text-align:center}
.hero-kicker{margin-top:81px;font-size:20px;letter-spacing:1px;color:var(--muted)}
.hero-title{margin-top:20px;font-family:var(--script);font-size:33px;line-height:40px;color:var(--ink);letter-spacing:1px}
.btn-dark{display:inline-block;background:var(--ink);color:#fff;font-size:13px;text-transform:uppercase;width:160px;height:40px;line-height:40px;text-align:center}
.hero-panel .btn-dark{margin-top:33px}
.hero-arrow{top:286px;width:52px;height:52px;border-radius:50%;background:rgba(255,255,255,.18)}
.hero-arrow svg{width:52px;height:52px;stroke:#fff;fill:none;stroke-width:1.4}

/* categories */
.categories{top:548px;left:0;width:1200px;height:545px;background:var(--pattern)}
.cat-card{top:84px;width:304px;height:403px;background:var(--paper);border:1px solid var(--line)}
.cat-image{width:304px;height:304px}
.cat-label{position:absolute;top:125px;left:40px;width:224px;height:55px;background:rgba(255,255,255,.8);font-family:var(--head);font-size:20px;color:var(--ink);text-align:center;line-height:55px;letter-spacing:1px}
.cat-text{padding:20px 14px 0;font-size:11px;line-height:14.5px;text-align:center;color:var(--text)}

/* featured */
.section-title{left:0;width:1200px;text-align:center;font-family:var(--head);font-size:25px;color:var(--ink);letter-spacing:1.5px}
.product{top:1258px;width:176px;text-align:center}
.product-image{position:relative;width:176px;height:192px}
.product-name{margin-top:22px;font-size:13px;color:var(--text)}
.product-price{margin-top:8px;font-size:13px;color:var(--ink)}
.product-hover{position:absolute;left:10px;bottom:10px;width:156px;height:58px;background:rgba(255,255,255,.75)}
.swatches{display:flex;gap:9px;justify-content:center;padding-top:8px}
.swatches span{width:14px;height:14px;border-radius:50%;border:1px solid #ccc}
.sizes{display:flex;gap:14px;justify-content:center;margin-top:10px;font-size:9.5px;color:var(--muted)}
.wish{position:absolute;top:8px;right:8px;width:18px;height:18px;stroke:var(--ink);fill:none;stroke-width:1.3}
.slide-arrow{width:22px;height:40px;stroke:#a9a9a9;fill:none;stroke-width:1.3}

/* about */
.about{top:1610px;left:0;width:1200px;height:328px;background:var(--band);text-align:center}
.about-title{margin-top:50px;font-family:var(--script);font-size:27px;color:var(--ink);letter-spacing:1px}
.about p{width:940px;margin:22px auto 0;font-size:13px;line-height:19.5px;color:var(--text);letter-spacing:.3px}
.about p:first-of-type{margin-top:36px}

/* news */
.post{top:2102px;width:304px;height:438px;background:var(--paper);border:1px solid var(--line)}
.post-image{position:relative;height:167px}
.post-date{position:absolute;top:8px;left:6px;background:rgba(255,255,255,.82);font-family:var(--script);font-size:14px;padding:2px 10px;color:var(--text)}
.post-meta{display:flex;justify-content:space-between;align-items:center;height:32px;padding:0 15px;border-bottom:1px solid var(--line);font-size:9.5px;text-transform:uppercase;color:var(--muted)}
.share{display:flex;gap:6px}
.share span{width:8px;height:8px;border-radius:50%;background:#555}
.post-title{padding:12px 15px 0;height:67px;font-family:var(--script);font-size:19.5px;line-height:24px;color:var(--ink)}
.post-text{padding:0 15px;height:80px;font-size:11px;line-height:14.5px;color:var(--muted)}
.post-comments{font-size:9.5px;text-transform:uppercase;color:var(--text);text-align:center;letter-spacing:.5px}
.post-comments::before{content:"";display:inline-block;width:8px;height:7px;border-radius:50%;background:var(--ink);margin-right:5px}
.btn-line{display:block;margin:16px auto 0;width:160px;height:40px;line-height:38px;text-align:center;border:1px solid var(--ink);font-size:13px;text-transform:uppercase;color:var(--ink)}
.btn-line.is-active{background:var(--ink);color:#fff}

/* footer */
.site-footer{top:2646px;left:0;width:1200px;height:311px;background:var(--footer);border-top:1px solid var(--line)}
.footer-brand{left:160px;top:110px;width:180px;text-align:center;font-size:24px;letter-spacing:1px;color:var(--ink)}
.footer-social{left:203px;top:156px;display:flex;gap:14px}
.footer-social span{width:11px;height:11px;border-radius:50%;background:var(--ink)}
.footer-col{top:56px}
.footer-col h3{font-family:var(--head);font-size:19px;color:var(--ink);letter-spacing:1.5px;font-weight:700}
.footer-col ul{list-style:none;margin-top:22px}
.footer-col li{font-size:12.5px;color:var(--text);margin-bottom:14px}
.contact-item{display:flex;gap:13px;margin-top:22px;font-size:12.5px;line-height:19px;color:var(--text)}
.contact-item svg{width:13px;height:13px;fill:var(--ink);margin-top:3px;flex:none}
.footer-bottom{top:2957px;left:0;width:1200px;height:33px;background:var(--bottom)}
.copyright{left:128px;top:10px;font-size:10.5px;color:#fff}
.payments{left:814px;top:9px;display:flex;gap:5px}
.payments span{width:24px;height:15px;background:#e9e9e9;border-radius:2px}
</style>
</head>
<body>

<header class="site-header abs">
  <a class="brand abs">VELORA CASA</a>
  <nav class="main-nav abs">
    <a>Front page</a><a class="has-sub">Women</a><a class="has-sub">Men</a><a class="has-sub">Children</a><a>About us</a><a>Contact</a>
  </nav>
  <div class="header-tools abs">
    <svg viewBox="0 0 18 18"><circle cx="7.5" cy="7.5" r="5.5"/><path d="M11.5 11.5L16 16"/></svg>
    <svg viewBox="0 0 18 18"><path d="M9 15.5S2 11 2 6.3A3.5 3.5 0 0 1 9 5a3.5 3.5 0 0 1 7 1.3C16 11 9 15.5 9 15.5z"/></svg>
    <span style="display:flex;align-items:center;gap:3px"><svg viewBox="0 0 18 18"><path d="M3 6h12l-1 10H4z"/><path d="M6 6V4.5a3 3 0 0 1 6 0V6"/></svg>(0)</span>
  </div>
</header>

<section class="hero abs" role="img" aria-label="Photo of a model in black lace lingerie set in a sunny garden">
  <div class="hero-arrow abs" style="left:62px"><svg viewBox="0 0 52 52"><path d="M30 16l-10 10 10 10"/></svg></div>
  <div class="hero-arrow abs" style="left:1085px"><svg viewBox="0 0 52 52"><path d="M22 16l10 10-10 10"/></svg></div>
</section>
<div class="hero-panel abs">
  <div class="hero-kicker">Lingerie</div>
  <div class="hero-title">Check out our new collection of<br>lingerie for women...</div>
  <a class="btn-dark">Take a look</a>
</div>

<section class="categories abs">
  <article class="cat-card abs" style="left:128px">
    <div class="cat-image" role="img" aria-label="Photo of a woman in a red push-up bra" style="background:linear-gradient(135deg,#7a5a4c,#c88e7a 40%,#b8213f 70%,#e8e2dc)"></div>
    <div class="cat-label">Women</div>
    <p class="cat-text">By coming to Velora casa, you will enter the wonderful world of lingerie. Intimate lingerie, invisible to many eyes, but always essential for the personal satisfaction</p>
  </article>
  <article class="cat-card abs" style="left:448px">
    <div class="cat-image" role="img" aria-label="Photo of a man in a grey t-shirt and striped boxers" style="background:linear-gradient(160deg,#4a4a4a,#7d7d7d 45%,#5f6266 75%,#3b4150)"></div>
    <div class="cat-label">Men</div>
    <p class="cat-text">Men's underwear for the modern man made of the highest quality cotton, soft to the touch and extremely comfortable to wear.</p>
  </article>
  <article class="cat-card abs" style="left:768px">
    <div class="cat-image" role="img" aria-label="Photo of a boy in a navy t-shirt and patterned shorts" style="background:linear-gradient(170deg,#e8e8e8,#c7b4a6 25%,#3b3f6e 55%,#5b6242 90%)"></div>
    <div class="cat-label">Children</div>
    <p class="cat-text">We pay special attention to the children's range of underwear, aware that only top quality underwear should be offered to children.</p>
  </article>
</section>

<h2 class="section-title abs" style="top:1182px">Featured products</h2>
<svg class="slide-arrow abs" style="left:85px;top:1336px" viewBox="0 0 22 40"><path d="M18 4L4 20l14 16"/></svg>
<svg class="slide-arrow abs" style="left:1093px;top:1336px" viewBox="0 0 22 40"><path d="M4 4l14 16L4 36"/></svg>

<div class="product abs" style="left:128px">
  <div class="product-image" role="img" aria-label="Product photo of a blush lace bra" style="background:linear-gradient(180deg,#f2ece8,#e6c9b8 50%,#f0e8e2)"></div>
  <div class="product-name">Corvella Gem Bra</div><div class="product-price">229.00 kn</div>
</div>
<div class="product abs" style="left:319px">
  <div class="product-image" role="img" aria-label="Product photo of a black men's t-shirt" style="background:linear-gradient(180deg,#f4f4f4,#1a1a1a 30%,#111 80%,#f4f4f4)"></div>
  <div class="product-name">Men's T-shirt Nautera 570</div><div class="product-price">89.00 kn</div>
</div>
<div class="product abs" style="left:512px">
  <div class="product-image" role="img" aria-label="Product photo of beige shaping shorts" style="background:linear-gradient(180deg,#e8d3b8,#d9bf9b 70%,#ece3d8)"></div>
  <div class="product-name">Women's shorts Ilvanne 108</div><div class="product-price">79.00 kn</div>
</div>
<div class="product abs" style="left:704px">
  <div class="product-image" role="img" aria-label="Product photo of nude seamless briefs" style="background:linear-gradient(180deg,#f3f3f3,#e9cbb4 45%,#eeeeee);border:1px solid var(--line)">
    <svg class="wish" viewBox="0 0 18 18"><path d="M9 15.5S2 11 2 6.3A3.5 3.5 0 0 1 9 5a3.5 3.5 0 0 1 7 1.3C16 11 9 15.5 9 15.5z"/></svg>
    <div class="product-hover">
      <div class="swatches"><span style="background:#fff"></span><span style="background:#222;border-color:#222"></span><span style="background:#e8262b;border-color:#e8262b"></span><span style="background:#3c74d6;border-color:#3c74d6"></span></div>
      <div class="sizes"><span>S/M</span><span>S-2</span><span>L</span><span>XL</span></div>
    </div>
  </div>
  <div class="product-name">Gaćice Lunelle 3324</div><div class="product-price">75.00 kn</div>
</div>
<div class="product abs" style="left:896px">
  <div class="product-image" role="img" aria-label="Product photo of a black lace garter belt" style="background:linear-gradient(180deg,#f5f5f5,#2a2a2a 25%,#555 55%,#f2f2f2 75%)"></div>
  <div class="product-name">Halter Serelia 1979</div><div class="product-price">169.00 kn</div>
</div>

<section class="about abs">
  <h2 class="about-title">Velora fashion - 20 years with you</h2>
  <p>At the location of the busiest shopping center in Marenvik - Aurentia center, the Velora casa boutique has been operating for 20 years. The store offers a large selection of favorite high-quality fashion lingerie brands for women, men and children.</p>
  <p>New in the offer! New collection of Italian Velatessa socks. Well-known Italian brand available in Croatia only in Velora casa stores. Various models , solid weaving, modern colors and patterns are just some of the qualities offered by Velatessa .</p>
  <p>Sophisticated lingerie , modern patterns and colors, made of high quality materials with selected details are named Ilvanne, Serelia, Sara Belmonte, Corvella, Lara Bellini, Lunelle, Liora, Matero, Kseniva, Galora, Arvis, Nautera, Dianova, Lovella, Jadessa , Multora, Pauvelle, Plexira, Velatessa.</p>
</section>

<h2 class="section-title abs" style="top:2027px">News</h2>
<svg class="slide-arrow abs" style="left:85px;top:2302px" viewBox="0 0 22 40"><path d="M18 4L4 20l14 16"/></svg>
<svg class="slide-arrow abs" style="left:1093px;top:2302px" viewBox="0 0 22 40"><path d="M4 4l14 16L4 36"/></svg>

<article class="post abs" style="left:128px">
  <div class="post-image" role="img" aria-label="Photo of a model in a turquoise lace bra by a waterfall" style="background:linear-gradient(90deg,#8a8f92,#3fa6b8 40%,#c9cdd0 70%,#9aa0a3)"><span class="post-date">06 March</span></div>
  <div class="post-meta"><span>Uncategorized</span><span class="share"><span></span><span></span><span></span></span></div>
  <h3 class="post-title">Discount on Women's Day with code: 15postodanzena</h3>
  <p class="post-text">Dear customers, take advantage of a 15% discount on our webshop and in our store at the Aurentia Center on the occasion of International Women's Day. The discount applies to the entire range, even to ...</p>
  <div class="post-comments">2 comments</div>
  <a class="btn-line">View post</a>
</article>
<article class="post abs" style="left:448px">
  <div class="post-image" role="img" aria-label="Photo of a model in a white strapless bra under palm trees" style="background:linear-gradient(90deg,#dfe6ea,#7f9a6b 35%,#c8d5dc 65%,#e7e1dc)"><span class="post-date">19 Feb</span></div>
  <div class="post-meta"><span>Discount</span><span class="share"><span></span><span></span><span></span></span></div>
  <h3 class="post-title">20-30% discount on part of the range</h3>
  <p class="post-text">Dear customers, stop by our store in the Aurentia Center and save 20-30% on certain items when buying. The discount is only in the store, not on the webshop. There is an ongoing discount of 20% on part of the ...</p>
  <div class="post-comments">5 comments</div>
  <a class="btn-line">View post</a>
</article>
<article class="post abs" style="left:768px">
  <div class="post-image" role="img" aria-label="Photo of a red wire heart with rose petals on pink" style="background:radial-gradient(circle at 50% 50%,#b8454a 0%,#d9a4a6 30%,#ead3d3 70%)"><span class="post-date">10 Feb</span></div>
  <div class="post-meta"><span>Discount</span><span class="share"><span></span><span></span><span></span></span></div>
  <h3 class="post-title">Discount for Valentine's Day with code: 15% VALENTINE'S DAY</h3>
  <p class="post-text">Dear customers, take advantage of a 15% discount on our webshop and in our store at the Aurentia Center on Valentine's Day. The discount applies to the entire range, even to already discounted items and to all ...</p>
  <div class="post-comments">0 comments</div>
  <a class="btn-line is-active">View post</a>
</article>

<footer class="site-footer abs">
  <div class="footer-brand abs">VELORA CASA</div>
  <div class="footer-social abs" aria-label="Social links"><span></span><span></span><span></span><span></span></div>
  <div class="footer-col abs" style="left:440px">
    <h3>Meet Us</h3>
    <ul><li>Terms of use</li><li>Terms of purchase</li><li>Security payment</li></ul>
  </div>
  <div class="footer-col abs" style="left:653px">
    <h3>Information</h3>
    <ul><li>Payment methods</li><li>Delivery</li><li>Returns and replacements</li></ul>
  </div>
  <div class="footer-col abs" style="left:896px">
    <h3>Contact</h3>
    <div class="contact-item"><svg viewBox="0 0 16 16"><path d="M3.5 1l3 3-1.8 1.8a9 9 0 0 0 5.5 5.5L12 9.5l3 3-2 2.5C7 14.5 1.5 9 1 3z"/></svg><span>Tel:<br>01 / 5550-123</span></div>
    <div class="contact-item"><svg viewBox="0 0 16 16"><path d="M1 3h14v10H1z"/><path d="M1 3l7 6 7-6" fill="none" stroke="#f4f4f4" stroke-width="1.3"/></svg><span>Mail:<br>info@veloracasa.hr</span></div>
    <div class="contact-item"><svg viewBox="0 0 16 16"><circle cx="8" cy="8" r="7"/><path d="M8 4v4l3 2" fill="none" stroke="#f4f4f4" stroke-width="1.4"/></svg><span>Working hours:<br>Mon - Sat: 09 - 21 h<br>Sun: Closed</span></div>
  </div>
</footer>
<div class="footer-bottom abs">
  <div class="copyright abs">© 2020 Velora Casa. Sva prava pridržana</div>
  <div class="payments abs" aria-label="Accepted payment methods"><span></span><span></span><span></span><span></span><span></span><span></span><span></span><span></span><span></span><span></span></div>
</div>

</body>
</html>
```